"1" Pager Webdesign + HTML Creation

In this project we ask you to create a Stepwise (the registration form will be opened on a second page) web design with the content & structure described in the attached PDF. You are absolutely free in your choice of colors & design. There is also no company logo on this site as it will serve as a demo site for future clients where the design & content can be adjusted.
Once we agree on the design we also ask you to convert it into a simple html page.
The site is not a regular company website with services etc. --> the main idea is to give client the ability to launch a dedicated server (VPS) fully automatically in the background from the web gui. This server will have a software installed that allows phishing simulations to test employees security awareness.....so there should be some logical flow from top to bottom that leads to the user to launch the server. The company details/ressources etc. are not important and can be really kept very small. Main point of the site is to explain user what the steps he needs to go through to launch that virtual server...so launch button must be also kinda big...
See example I created (jpg) --> I am not designer. This is just to illustrate what I mean with logical "flow"....
As for pricing: I don't expect a fully functional html site & finished design for this price and I am willing to pay an extra bonus for finalizing the design/site as I know the details are time consuming. This bonus could be agreed upon project start and paid via zenvora. What I want are a few design examples that show that you understood what I need. Depending how much custom graphics need to be created we can discuss extra bonus/time required...
The site is not a regular company website with services etc. --> the main idea is to give client the ability to launch a dedicated server (VPS) fully automatically in the background from the web gui. This server will have a software installed that allows phishing simulations to test employees security awareness.....so there should be some logical flow from top to bottom that leads to the user to launch the server.... Added Thursday, August 11, 2016
Coding
Coded - Design and coding required
Number of Pages Required
2 page
Look and feel

```html
<!DOCTYPE html>
<html lang="en">
<head>
<meta charset="utf-8">
<title>Stepwise – Phishing Simulation Platform</title>
<link href="https://fonts.googleapis.com/css2?family=Roboto:wght@300;400;500;700&family=Montserrat:wght@400;600;700;800&display=swap" rel="stylesheet">
<style>
:root{
  --orange:#e9643f;
  --blue:#2f86d6;
  --sky:#3a9be6;
  --dark:#3b3e45;
  --darker:#2e3036;
  --ink:#2b2b2b;
  --muted:#8a8a8a;
  --light:#f2f2f2;
  --line:#dcdcdc;
  --white:#ffffff;
  --measure:#3d9be3;
  --train:#ef7f63;
}
*{box-sizing:border-box;margin:0;padding:0}
html,body{width:1200px;height:4500px;overflow:hidden}
body{position:relative;font-family:"Roboto",Arial,sans-serif;color:var(--ink);background:var(--white)}
.abs{position:absolute}
.btn{position:absolute;background:var(--orange);color:var(--white);font:500 15px "Roboto",sans-serif;letter-spacing:1px;text-transform:uppercase;display:flex;align-items:center;justify-content:center;gap:10px}
.center{left:0;width:1200px;text-align:center}

/* hero */
.hero{top:0;left:0;width:1200px;height:690px;background:linear-gradient(180deg,#55585f 0%,#6d7078 55%,#5e6168 100%)}
.topbar{top:0;left:0;width:1200px;height:108px;background:rgba(40,42,48,.55)}
.brand{top:30px;left:90px;display:flex;align-items:center;gap:14px;color:var(--white);font:700 30px "Montserrat",sans-serif;letter-spacing:2px}
.brand-box{width:46px;height:46px;border:3px solid var(--white)}
.nav{top:42px;left:390px;display:flex;gap:30px;color:var(--white);font:500 14px "Roboto",sans-serif;text-transform:uppercase}
.hero-title{top:385px;color:var(--white);font:400 46px "Roboto",sans-serif}
.play{top:270px;left:555px;width:90px;height:90px;border:3px solid var(--white);border-radius:50%}
.start{top:598px;color:var(--white);font:700 17px "Roboto",sans-serif;letter-spacing:2px}
.plus{top:630px;color:var(--white);font:700 22px "Roboto",sans-serif}

/* intro */
.intro-title{top:752px;font:500 32px/1.45 "Roboto",sans-serif;color:var(--ink)}
.side-title{font:400 25px "Roboto",sans-serif;color:var(--ink)}
.side-text{font:300 14px/1.5 "Roboto",sans-serif;color:var(--muted)}
.how{top:1172px;color:var(--orange);font:500 17px "Roboto",sans-serif;letter-spacing:2px}

/* dark band */
.band{top:1270px;left:0;width:1200px;height:260px;background:linear-gradient(90deg,#4a4c51,#6a6c70 50%,#55575b)}
.band-text{top:1330px;left:300px;width:600px;text-align:center;color:var(--white);font:300 25px/1.35 "Roboto",sans-serif}

/* tabs */
.tab{position:absolute;top:1530px;height:42px;width:400px;display:flex;align-items:center;justify-content:center;font:500 15px "Roboto",sans-serif;letter-spacing:2px;border:2px solid var(--line);background:var(--white);color:var(--ink)}
.tab.active{background:var(--blue);border-color:var(--blue);color:var(--white)}

/* step */
.step{top:1572px;left:0;width:1200px;height:568px;background:var(--light)}
.step-art{top:1620px;left:200px;width:380px;height:380px;background:linear-gradient(160deg,#eef2f5,#dfe6ec);border-radius:4px}
.step-title{top:1646px;left:614px;font:500 29px "Roboto",sans-serif}
.step-sub{top:1686px;left:614px;font:400 16px "Roboto",sans-serif;color:#555}
.checks{top:1752px;left:614px;list-style:none}
.checks li{display:flex;gap:16px;margin-bottom:20px}
.checks b{display:block;font:400 16px "Roboto",sans-serif;color:#666}
.checks small{font:400 12px "Roboto",sans-serif;color:#444}
.explore{top:2026px;left:614px;width:186px;height:40px;background:#c9cbcd;color:var(--white);font:500 14px "Roboto",sans-serif;letter-spacing:1px;display:flex;align-items:center;justify-content:center}

/* launch */
.launch{top:2140px;left:0;width:1200px;height:370px;background:linear-gradient(180deg,#2f8ce0,#45a6ee 70%,#dcefff 100%)}
.launch-word{top:2278px;color:var(--white);font:700 70px "Montserrat",sans-serif;letter-spacing:1px}
.rocket{top:2170px;left:520px;width:160px;height:300px;background:linear-gradient(180deg,#f06a4a,#f7b23c);border-radius:80px 80px 20px 20px;opacity:.85}
.launch-title{top:2568px;font:500 29px/1.4 "Roboto",sans-serif}

/* resources */
.res{top:2805px;left:0;width:1200px;height:685px;background:var(--light)}
.res-title{top:2868px;font:500 29px "Roboto",sans-serif}
.card{top:2940px;width:412px;height:488px;background:var(--white)}
.card-art{width:412px;height:186px}
.card h3{position:absolute;top:210px;left:30px;font:400 23px "Roboto",sans-serif}
.card p{position:absolute;top:252px;left:30px;width:340px;font:400 14px/1.45 "Roboto",sans-serif;color:#c0603f}
.card .btn{top:360px;left:30px;width:186px;height:36px;font-size:13px}

/* map */
.map{top:3490px;left:0;width:1200px;height:230px;background:linear-gradient(120deg,#4d9ad8,#5ea8e2 50%,#4a94d2)}

/* contact */
.contact-col{position:absolute;top:3770px;width:300px;text-align:center}
.contact-col p{font:400 14px/1.4 "Roboto",sans-serif;color:#555;margin-top:12px}
.phone{font:400 23px "Roboto",sans-serif;color:#555}
.link{color:var(--blue);text-decoration:underline}
.rule{top:3975px;height:1px;background:var(--line)}
.q-title{top:3955px;left:450px;width:300px;text-align:center;background:var(--white);font:500 31px "Roboto",sans-serif}

/* form */
.field{position:absolute;border:1px solid var(--line);background:var(--white);height:38px;padding:10px 12px;font:400 13px "Roboto",sans-serif;color:#b5b5b5}
.submit{top:4290px;left:262px;width:676px;height:40px}

/* footer */
.footer{top:4410px;left:0;width:1200px;height:90px;background:var(--darker)}
.foot-text{top:4445px;left:90px;color:#cfcfcf;font:400 14px "Roboto",sans-serif}
.foot-text span{color:var(--orange)}
.social{top:4436px;display:flex;gap:10px;left:968px}
.social i{display:block;width:30px;height:30px;border:1px solid #9a9a9a;border-radius:50%}
.to-top{top:4355px;left:1143px;width:30px;height:30px;border-radius:50%;background:var(--orange)}
</style>
</head>
<body>

<!-- hero -->
<div class="abs hero" role="img" aria-label="Hero illustration of a laptop surrounded by flat icons of charts, mail, music and media on a grey background"></div>
<header class="abs topbar"></header>
<div class="abs brand"><span class="brand-box"></span>STEPWISE</div>
<nav class="abs nav"><span>Home</span><span>About us</span><span>How it works</span><span>Ressources</span><span>Contact us</span></nav>
<div class="btn" style="top:38px;left:955px;width:156px;height:40px;font-size:13px">Get started</div>
<svg class="abs play" viewBox="0 0 90 90"><polygon points="36,28 62,45 36,62" fill="none" stroke="#fff" stroke-width="3"/></svg>
<h1 class="abs center hero-title">In 10 Minutes from Start to Phish!</h1>
<div class="btn" style="top:466px;left:510px;width:180px;height:38px;font-size:12px">Watch the video</div>
<div class="abs center start">START NOW</div>
<div class="abs center plus">+</div>

<!-- intro -->
<h2 class="abs center intro-title">Build your best Human Phishing and<br>Malware Defense with us</h2>
<div class="abs side-title" style="top:942px;left:255px">Test your users</div>
<p class="abs side-text" style="top:978px;left:140px;width:280px;text-align:right">Fully automated Spear Phishing, Malware, Smishing, and USB attack Simulations</p>
<div class="abs side-title" style="top:942px;left:790px">Train your users</div>
<p class="abs side-text" style="top:978px;left:790px;width:300px">Choose among many ondemand interactive, engaging training modules (customizable tips, video's, games, quiz etc.)</p>
<svg class="abs" style="top:860px;left:410px" width="380" height="300" viewBox="0 0 380 300">
  <path d="M150 30 Q190 5 230 30" fill="none" stroke="#3d9be3" stroke-width="3"/>
  <polygon points="230,30 218,28 226,20" fill="#3d9be3"/>
  <path d="M230 270 Q190 295 150 270" fill="none" stroke="#ef7f63" stroke-width="3"/>
  <polygon points="150,270 162,272 154,280" fill="#ef7f63"/>
  <circle cx="120" cy="150" r="103" fill="#3d9be3"/>
  <circle cx="260" cy="150" r="103" fill="#ef7f63" fill-opacity=".92"/>
  <text x="105" y="198" fill="#fff" font-family="Roboto,sans-serif" font-size="13" letter-spacing="1">MEASURE</text>
  <text x="262" y="198" fill="#fff" font-family="Roboto,sans-serif" font-size="13" letter-spacing="1">TRAIN</text>
</svg>
<div class="abs center how">HOW IT WORKS?</div>
<svg class="abs" style="top:1205px;left:596px" width="8" height="70"><line x1="4" y1="0" x2="4" y2="70" stroke="#e9643f" stroke-width="2"/></svg>

<!-- band -->
<div class="abs band" role="img" aria-label="Dimmed photo of hands typing on a keyboard"></div>
<p class="abs band-text">It's so easy. After registration you can launch a virtualized server with a full scale testing and education platform within minutes.</p>
<svg class="abs" style="top:1380px;left:0" width="1200" height="130">
  <g stroke="#fff" stroke-width="2" stroke-dasharray="6 6" fill="none">
    <polyline points="280,0 200,0 200,115"/>
    <polyline points="920,0 1000,0 1000,115"/>
    <line x1="600" y1="60" x2="600" y2="115"/>
  </g>
  <g fill="#fff"><polygon points="194,112 206,112 200,124"/><polygon points="994,112 1006,112 1000,124"/><polygon points="594,112 606,112 600,124"/></g>
</svg>

<!-- tabs -->
<div class="tab active" style="left:0">STEP 1</div>
<div class="tab" style="left:400px">STEP 2</div>
<div class="tab" style="left:800px">STEP 3</div>

<!-- step -->
<section class="abs step"></section>
<svg class="abs" style="top:1570px;left:188px" width="24" height="14"><polygon points="0,0 24,0 12,14" fill="#2f86d6"/></svg>
<div class="abs step-art" role="img" aria-label="Illustration of a businessman looking at a red signpost with several directions"></div>
<h3 class="abs step-title">Basic Settings</h3>
<p class="abs step-sub">Choose Your Preferred Campaign Settings</p>
<ul class="abs checks">
  <li><svg width="28" height="28" viewBox="0 0 28 28"><circle cx="14" cy="14" r="12" fill="none" stroke="#2f86d6" stroke-width="2"/><polyline points="8,14 12,18 20,10" fill="none" stroke="#2f86d6" stroke-width="2.5"/></svg><div><b>Duration of campaign</b><small>up to 3 years</small></div></li>
  <li><svg width="28" height="28" viewBox="0 0 28 28"><circle cx="14" cy="14" r="12" fill="none" stroke="#2f86d6" stroke-width="2"/><polyline points="8,14 12,18 20,10" fill="none" stroke="#2f86d6" stroke-width="2.5"/></svg><div><b>Number of employees to test/train</b><small>..</small></div></li>
  <li><svg width="28" height="28" viewBox="0 0 28 28"><circle cx="14" cy="14" r="12" fill="none" stroke="#2f86d6" stroke-width="2"/><polyline points="8,14 12,18 20,10" fill="none" stroke="#2f86d6" stroke-width="2.5"/></svg><div><b>Technical details</b><small>Domain names etc.</small></div></li>
  <li><svg width="28" height="28" viewBox="0 0 28 28"><circle cx="14" cy="14" r="12" fill="none" stroke="#2f86d6" stroke-width="2"/><polyline points="8,14 12,18 20,10" fill="none" stroke="#2f86d6" stroke-width="2.5"/></svg><div><b>Choose additional services</b><small>Campaign setup support etc.</small></div></li>
</ul>
<div class="abs explore">EXPLORE MORE</div>

<!-- launch -->
<div class="abs launch" role="img" aria-label="Blue sky illustration with white clouds"></div>
<div class="abs rocket" role="img" aria-label="Illustration of a red rocket taking off"></div>
<div class="abs launch-word" style="left:300px">LAUNCH</div>
<div class="abs launch-word" style="left:690px">SERVER</div>
<h2 class="abs center launch-title">Launch Your Virtualized Security Awareness<br>Training and Phishing/Malware Simulation Platform</h2>
<div class="btn" style="top:2672px;left:483px;width:234px;height:54px;font-size:16px">Register now!</div>

<!-- resources -->
<section class="abs res"></section>
<h2 class="abs center res-title">Ressources</h2>
<div class="abs card" style="left:175px">
  <div class="card-art" role="img" aria-label="Flat illustration of security icons: padlock, shield, keyboard and folders on teal" style="background:linear-gradient(135deg,#2ec4a5,#27b596)"></div>
  <h3>Our Services</h3>
  <p>when an unknown printer took a galley of type and scrambled it to make a type specimen book. It has survived not only five centuries, but also the leap into electronic typesetting, remaining essentially unchanged.</p>
  <div class="btn">&#x2913; About us PDF</div>
</div>
<div class="abs card" style="left:615px">
  <div class="card-art" role="img" aria-label="Flat illustration of a team of three business people" style="background:linear-gradient(135deg,#7e84b5,#676ea3)"></div>
  <h3>About US</h3>
  <p>when an unknown printer took a galley of type and scrambled it to make a type specimen book. It has survived not only five centuries, but also the leap into electronic typesetting, remaining essentially unchanged.</p>
  <div class="btn">&#x2913; About us PDF</div>
</div>

<!-- map -->
<div class="abs map" role="img" aria-label="Street map showing the office location"></div>
<svg class="abs" style="top:3578px;left:586px" width="28" height="40" viewBox="0 0 28 40"><path d="M14 0C6 0 0 6 0 14c0 10 14 26 14 26s14-16 14-26C28 6 22 0 14 0z" fill="#fff"/><circle cx="14" cy="14" r="5" fill="#5ea8e2"/></svg>

<!-- contact -->
<div class="contact-col" style="left:165px">
  <svg width="34" height="34" viewBox="0 0 34 34"><path d="M17 3c-6 0-10 4-10 10 0 8 10 18 10 18s10-10 10-18c0-6-4-10-10-10z" fill="none" stroke="#2f86d6" stroke-width="2"/><circle cx="17" cy="13" r="3.5" fill="none" stroke="#2f86d6" stroke-width="2"/></svg>
  <p>27 Harbor Lane, Westfield<br>Lorem City, LM 94107</p>
</div>
<div class="contact-col" style="left:450px">
  <svg width="34" height="34" viewBox="0 0 34 34"><rect x="10" y="3" width="14" height="28" rx="3" fill="none" stroke="#2f86d6" stroke-width="2"/><line x1="15" y1="26" x2="19" y2="26" stroke="#2f86d6" stroke-width="2"/></svg>
  <div class="phone" style="margin-top:6px">1 - 800 - 555 - 0142</div>
  <p style="margin-top:2px" class="link">help@stepwise.example</p>
</div>
<div class="contact-col" style="left:735px">
  <svg width="34" height="34" viewBox="0 0 34 34"><circle cx="17" cy="17" r="13" fill="none" stroke="#2f86d6" stroke-width="2"/><circle cx="17" cy="17" r="6" fill="none" stroke="#2f86d6" stroke-width="2"/></svg>
  <p>Need Help or Support?<br><span class="link">Contact Us</span></p>
</div>

<div class="abs rule" style="left:90px;width:1020px"></div>
<h2 class="abs q-title">Have a Question?</h2>

<!-- form -->
<div class="field" style="top:4055px;left:262px;width:328px">Name</div>
<div class="field" style="top:4055px;left:610px;width:328px">Email</div>
<div class="field" style="top:4110px;left:262px;width:328px">Phone</div>
<div class="field" style="top:4110px;left:610px;width:328px;display:flex;justify-content:space-between">Category<span>&#9662;</span></div>
<div class="field" style="top:4165px;left:262px;width:676px;height:108px">Message</div>
<div class="btn submit">Submit</div>

<div class="abs to-top"></div>
<svg class="abs" style="top:4364px;left:1151px" width="14" height="10"><polyline points="2,8 7,3 12,8" fill="none" stroke="#fff" stroke-width="2"/></svg>

<!-- footer -->
<footer class="abs footer"></footer>
<p class="abs foot-text"><span>Stepwise</span> © 2016 All Right Reserved <span>Terms of Use</span> and <span>Privacy Policy</span></p>
<div class="abs social"><i></i><i></i><i></i><i></i></div>

</body>
</html>
```